Design Ridgeway Saddle Club's clubhouse Third Bridle Sign

Looking to design the Third Bridle clubhouse signage for Ridgeway Saddle Club. This will be a one color metal sign that will be placed on the entrance wall next to the entry door. See attached examples, looking for a vector file.

Would like to incorporate the Ridgeway Saddle Club Logo or elements of it but open to other ideas and the name of the clubhouse is the Third Bridle - verbiage can be Ridgeway Saddle Club- Club house or open to another term depending on design. This will be used to identify the space that will be used by the players and patrons. the clubhouse will be used by players go to mingle, get drinks and watch polo.

Target Market(s)

polo player club lounge for players and patrons to go mingle have drinks.

Colors

Designer to choose only greyscale colors for use in the design.

Requirements
Must have
• the name - Third Bridle

```html
<!DOCTYPE html>
<html lang="en">
<head>
<meta charset="utf-8">
<title>Third Bridle – Ridgeway Saddle Club Clubhouse Sign</title>
<link rel="stylesheet" href="https://fonts.googleapis.com/css2?family=Anton&display=swap">
<style>
  :root {
    --page-bg: #f2f2f2;
    --panel-light: #f1e8de;
    --panel-mid: #e8dccd;
    --panel-edge: #d6c2a8;
    --ink: #1e1e1e;
    --ink-reverse: #f4ebe2;
    --frame-line: #2a2a2a;
  }
  * { box-sizing: border-box; margin: 0; padding: 0; }
  html, body {
    width: 800px;
    height: 1200px;
    overflow: hidden;
    background: var(--page-bg);
  }
  .canvas {
    position: relative;
    width: 800px;
    height: 1200px;
  }
  .sign-panel {
    position: absolute;
    left: 50px;
    top: 180px;
    width: 700px;
    height: 840px;
    background:
      radial-gradient(ellipse at 50% 45%, var(--panel-light) 0%, var(--panel-mid) 62%, var(--panel-edge) 100%);
    box-shadow: 0 6px 22px rgba(0, 0, 0, 0.18);
  }
  .sign-frame {
    position: absolute;
    left: 31px;
    top: 37px;
    right: 31px;
    bottom: 38px;
    border: 1.5px solid var(--frame-line);
    display: flex;
    flex-direction: column;
    align-items: center;
  }
  .club-name-area {
    height: 415px;
    width: 100%;
    display: flex;
    align-items: center;
    justify-content: center;
  }
  .club-name {
    font-family: "Anton", sans-serif;
    font-weight: 400;
    font-size: 46px;
    letter-spacing: 3px;
    color: var(--ink);
    text-transform: uppercase;
    text-align: center;
    line-height: 1.15;
  }
  .clubhouse-name {
    font-family: "Anton", sans-serif;
    font-weight: 400;
    font-size: 98px;
    line-height: 1;
    letter-spacing: 1px;
    color: var(--ink);
    text-transform: uppercase;
    margin-top: 0;
  }
  .phone-band {
    margin-top: 22px;
    width: 565px;
    height: 123px;
    background: var(--ink);
    display: flex;
    align-items: center;
    justify-content: center;
  }
  .phone-number {
    font-family: "Anton", sans-serif;
    font-size: 86px;
    line-height: 1;
    letter-spacing: 2px;
    color: var(--ink-reverse);
  }
  .web-address {
    margin-top: 22px;
    font-family: "Anton", sans-serif;
    font-size: 30px;
    letter-spacing: 3px;
    color: var(--ink);
  }
</style>
</head>
<body>
  <main class="canvas">
    <section class="sign-panel">
      <div class="sign-frame">
        <div class="club-name-area">
          <p class="club-name">Ridgeway Saddle Club</p>
        </div>
        <h1 class="clubhouse-name">Third Bridle</h1>
        <div class="phone-band">
          <p class="phone-number">555-214-0187</p>
        </div>
        <p class="web-address">www.ridgewaysaddle.com</p>
      </div>
    </section>
  </main>
</body>
</html>
```